Brantley Metal Roofing INC.

Hello,
I am working with a local business to design them a new website. The designer I had worked with moved to colorado and has taken a new job. He recommended that I try posting my new jobs on here. I would need a design and assistance setting the site up on my hostmerry server. I work by myself and handle the sales side of things and need a designer that can help me out.
This company is a metal roofing business. The current page I made for them is www.brantleymetalinc.example

They would like the new site to be similar to http://www.dovecreekalloy.example

Please let me know if this is something that you could do for us.
Updates

the company wants the site to look very similar to this http://www.dovecreekalloy.exampleis that something you could do, please get in touch with me.Thanks Added Tuesday, January 10, 2017

Industry/Entity Type

Business

Font styles to use
Sans Serif

Colors
ed252d

Requirements
Must have
• the company wants the site to look very similar to this
• http://www.dovecreekalloy.example
• is that something you could do, please get in touch with me.
• Thanks

```html
<!DOCTYPE html>
<html lang="en">
<head>
<meta charset="utf-8">
<title>Brantley Metal Inc</title>
<link href="https://fonts.googleapis.com/css2?family=Open+Sans:wght@400;600;700&display=swap" rel="stylesheet">
<style>
:root{
  --red:#ed252d;
  --red-dark:#c81e25;
  --admin:#23282d;
  --ink:#222;
  --muted:#666;
  --page:#e6e6e6;
  --panel:#f0f0f0;
  --white:#fff;
}
*{margin:0;padding:0;box-sizing:border-box}
html,body{width:821px;height:1200px;overflow:hidden}
body{position:relative;background:var(--page);font-family:"Open Sans",Arial,sans-serif;color:var(--ink)}
.abs{position:absolute}
.admin-bar{left:0;top:0;width:821px;height:20px;background:var(--admin);color:#eee;font-size:8px;display:flex;align-items:center;padding:0 6px;gap:12px}
.admin-bar .dot{width:11px;height:11px;border-radius:50%;background:#9ea3a8;display:inline-block}
.admin-bar .dot.violet{background:#7e3bd0}
.admin-bar .right{margin-left:auto}
.top-bar{left:0;top:20px;width:821px;height:21px;background:var(--red);color:var(--white);font-size:7.5px;font-weight:600;display:flex;align-items:center;padding-left:92px;gap:10px}
.top-bar svg{vertical-align:-1px;margin-right:2px}
.header{left:0;top:41px;width:821px;height:42px;background:var(--white);box-shadow:0 1px 2px rgba(0,0,0,.08)}
.brand{left:94px;top:11px;width:94px;height:21px;border:1.5px solid #222;font-size:7.5px;display:flex;align-items:center;justify-content:center;letter-spacing:.2px;color:#333}
.nav{left:266px;top:0;height:42px;display:flex;align-items:center;gap:0;font-size:8px;font-weight:600;color:#555}
.nav span{margin-right:33px}
.nav .active{color:var(--red)}
.hero-photo{left:107px;top:130px;width:477px;height:295px;background:linear-gradient(180deg,#a9c6e8 0%,#c9dbee 45%,#9a9a92 60%,#7d7f78 85%,#6f8f3f 100%)}
.hero-side{left:584px;top:130px;width:138px;height:295px;background:var(--panel);overflow:hidden;font-size:7px;line-height:16px;color:#333}
.hero-side .item{padding:10px 12px 8px}
.hero-side .item.current{background:#e2e2e2}
.hero-side b{font-weight:700;color:#222}
.hero-arrow{left:577px;top:160px}
.divider{left:179px;top:474px;width:457px;height:2px;background:linear-gradient(90deg,transparent,#cfcfcf 20%,#cfcfcf 80%,transparent)}
.card{top:565px;width:180px;text-align:center}
.card .pic{width:180px;height:180px;border:2px solid var(--white);box-shadow:0 0 2px rgba(0,0,0,.15)}
.card h3{font-size:10px;font-weight:700;line-height:17px;margin-top:17px;padding:0 -10px}
.card p{font-size:7.8px;line-height:16px;margin-top:14px;color:#333}
.footer{left:0;top:894px;width:821px;height:272px;background:var(--red);color:var(--white)}
.footer h4{position:absolute;top:44px;font-size:11px;font-weight:400}
.svc{position:absolute;left:91px;display:flex;align-items:center;gap:7px;font-size:7px;font-weight:700;line-height:16px}
.svc .thumb{width:40px;height:40px;border-radius:50%;border:2px solid var(--white);flex:none}
.links{position:absolute;left:259px;top:73px;list-style:none;font-size:7.5px;line-height:19.7px}
.links li::before{content:"";display:inline-block;width:3px;height:3px;border-radius:50%;background:var(--white);margin-right:6px;vertical-align:2px}
.hours{position:absolute;left:428px;top:71px;font-size:7.5px;line-height:16px;width:150px}
.contact{position:absolute;left:597px;top:71px;font-size:7.5px;line-height:16px;width:150px}
.bottom{left:0;top:1166px;width:821px;height:34px;background:var(--red-dark);color:var(--white);font-size:7.5px;display:flex;align-items:center;justify-content:center}
</style>
</head>
<body>
<div class="abs admin-bar">
  <span class="dot"></span><span>My Blog</span><span>0</span><span>+ New</span><span>Edit Page</span><span class="dot violet"></span><span>Enable Visual Builder</span>
  <span class="right">Howdy, admin</span>
</div>
<div class="abs top-bar">
  <span><svg width="7" height="7" viewBox="0 0 10 10"><path d="M2 0.5l2 2.5-1 1.2c.6 1.3 1.5 2.2 2.8 2.8l1.2-1 2.5 2-1 1.5C4.5 9.5.5 5.5.5 1.5z" fill="#fff"/></svg>555-014-0765 FAX: 555-014-4931</span>
  <span><svg width="8" height="6" viewBox="0 0 10 7"><rect width="10" height="7" fill="#fff"/><path d="M0 0l5 4 5-4" stroke="#ed252d" fill="none"/></svg>support@brantley-metal-inc.hostmerrysites.example</span>
</div>
<div class="abs header">
  <div class="abs brand">BRANTLEY METAL INC</div>
  <nav class="abs nav"><span class="active">HOME</span><span>ABOUT US</span><span>PRODUCTS</span><span>PROJECT GALLERY</span><span>CONTACT US</span><span>GET A QUOTE</span></nav>
</div>
<div class="abs hero-photo" role="img" aria-label="Photo of a large two-storey post frame metal building with porch under a blue sky"></div>
<div class="abs hero-side">
  <div class="item current"><b>BRANTLEY METAL INC</b><br>MANUFACTURERS OF QUALITY BUILDING COMPONENTS</div>
  <div class="item"><b>COMPLETE POST FRAME BUILDING PACKAGES</b><br>CALL US FOR A QUOTE, OR STOP IN AND WE CAN HELP YOU</div>
  <div class="item"><b>RESIDENTIAL METAL ROOFING</b><br>SUPER RIB, SNAP-LOC AND A VARIETY OF METAL ROOFING OPTIONS.</div>
  <div class="item"><b>COMMERCIAL AND AGRICULTURAL APPLICATIONS</b><br>28 GAUGE PANELS ARE THE THICKEST AND STRONGEST IN THE INDUSTRY.</div>
</div>
<svg class="abs hero-arrow" width="8" height="14" viewBox="0 0 8 14"><path d="M8 0L0 7l8 7z" fill="#e2e2e2"/></svg>
<div class="abs divider"></div>

<section class="abs card" style="left:107px">
  <div class="pic" role="img" aria-label="Photo of timber roof trusses against a blue sky" style="background:linear-gradient(160deg,#7fb0e0,#d9a56a 55%,#c98a4e)"></div>
  <h3>COMPLETE POST FRAME BUILDING PACKAGES</h3>
  <p>CALL US FOR A QUOTE, OR STOP IN AND WE CAN HELP YOU DESIGN.</p>
</section>
<section class="abs card" style="left:320px">
  <div class="pic" role="img" aria-label="Photo of a house with a grey standing seam metal roof" style="background:linear-gradient(150deg,#f4f4f4 20%,#a8b4b4 45%,#7a4b35 75%,#5d3827)"></div>
  <h3>RESIDENTIAL METAL ROOFING</h3>
  <p>SUPER RIB, SNAP-LOC AND A VARIETY OF METAL ROOFING OPTIONS.</p>
</section>
<section class="abs card" style="left:535px">
  <div class="pic" role="img" aria-label="Photo of a commercial building with red metal roof and tan wall panels" style="background:linear-gradient(180deg,#8aa0c0 0%,#7c3a3c 22%,#b9ab8e 50%,#a08b70 80%,#8d4a3c)"></div>
  <h3>COMMERCIAL AND AGRICULTURAL APPLICATIONS</h3>
  <p>28 GAUGE PANELS ARE THE THICKEST AND STRONGEST IN THE INDUSTRY.</p>
</section>

<footer class="abs footer">
  <h4 style="left:91px">Our Services</h4>
  <h4 style="left:259px">Quick Links</h4>
  <h4 style="left:428px">Working Hours</h4>
  <h4 style="left:597px">Contact Us</h4>
  <div class="svc" style="top:67px"><div class="thumb" role="img" aria-label="Roof trusses thumbnail" style="background:#c98a4e"></div><span>COMPLETE POST FRAME<br>BUILDING PACKAGES</span></div>
  <div class="svc" style="top:119px"><div class="thumb" role="img" aria-label="Metal roofing thumbnail" style="background:#9aa5a8"></div><span>RESIDENTIAL METAL<br>ROOFING</span></div>
  <div class="svc" style="top:171px"><div class="thumb" role="img" aria-label="Commercial building thumbnail" style="background:#8d6a5a"></div><span>COMMERCIAL AND<br>AGRICULTURAL<br>APPLICATIONS</span></div>
  <ul class="links"><li>Home</li><li>About Us</li><li>Products</li><li>Project Gallery</li><li>Contact Us</li><li>Get a Quote</li></ul>
  <div class="hours"><b>Better yet, see us in person!</b><br>We love our customers, so feel free to visit during normal business hours.<br><b>Hours</b><br>Monday - Friday: 7am - 5pm<br>Saturday: 7AM - 12PM<br>Sunday: Closed</div>
  <div class="contact">BRANTLEY METAL INC PHONE : 555-014-0765 FAX : 555-014-4931</div>
</footer>
<div class="abs bottom">Copyright © 2016 BRANTLEY METAL INC - All Rights Reserved.</div>
</body>
</html>
```